Corvane Industries business cards

We need business cards for our company Corvane Industries, based in Brisbane but trading world wide. We buy and sell Corvane Industries, generators and marine equipment. The design needs to be kept clean, simple but eye catching.
Please keep with our current logo (included) and further information can be included on request

Business

0792cd
33a6d7
85cae6
3276b5
0455a3
cedeed
cee9f5
ffffff

```html
<!DOCTYPE html>
<html lang="en">
<head>
<meta charset="UTF-8">
<title>Corvane Industries – Business Card</title>
<link href="https://fonts.googleapis.com/css2?family=Arimo:wght@400;700&display=swap" rel="stylesheet">
<style>
  :root {
    --navy: #0455a3;
    --royal: #3276b5;
    --sky: #33a6d7;
    --ice: #cee9f5;
    --ice-deep: #b9def0;
    --mist: #cedeed;
    --white: #ffffff;
    --backdrop: #e6ebf0;
  }
  html, body {
    margin: 0;
    padding: 0;
    width: 1200px;
    height: 803px;
    overflow: hidden;
    background: var(--backdrop);
    font-family: "Arimo", Arial, sans-serif;
  }
  .card {
    position: absolute;
    left: 100px;
    top: 96px;
    width: 1000px;
    height: 610px;
    background: linear-gradient(160deg, var(--ice) 0%, var(--ice-deep) 100%);
    box-shadow: 0 12px 30px rgba(4, 85, 163, 0.18);
    color: var(--navy);
  }
  .brand {
    position: absolute;
    left: 48px;
    top: 62px;
    display: flex;
    align-items: center;
    gap: 26px;
  }
  .brand-mark {
    width: 150px;
    height: 150px;
    border-radius: 18px;
    background: var(--navy);
  }
  .brand-name {
    font-weight: 700;
    font-size: 58px;
    line-height: 1;
    color: var(--navy);
    margin: 0;
  }
  .brand-suffix {
    display: block;
    font-size: 18px;
    font-weight: 400;
    color: var(--navy);
    text-align: right;
    margin-top: 6px;
  }
  .person {
    position: absolute;
    right: 56px;
    top: 62px;
    margin: 0;
    font-size: 40px;
    font-weight: 700;
    color: var(--royal);
  }
  .contact-list {
    position: absolute;
    right: 56px;
    top: 218px;
    list-style: none;
    margin: 0;
    padding: 0;
    font-size: 27px;
    font-weight: 700;
    color: var(--navy);
  }
  .contact-list li {
    display: flex;
    align-items: center;
    justify-content: flex-end;
    gap: 12px;
    height: 38px;
  }
  .contact-icon { width: 26px; height: 26px; fill: var(--sky); }
  .address {
    position: absolute;
    left: 160px;
    top: 380px;
    margin: 0;
    font-style: normal;
    font-size: 35px;
    font-weight: 700;
    line-height: 1.25;
    color: var(--navy);
  }
  .address span { display: block; }
  .address .po { padding-left: 50px; }
  .website {
    position: absolute;
    right: 50px;
    top: 496px;
    font-size: 26px;
    font-weight: 700;
    color: var(--sky);
  }
  .email {
    position: absolute;
    left: 26px;
    bottom: 30px;
    font-size: 26px;
    font-weight: 700;
    color: var(--sky);
  }
</style>
</head>
<body>
  <article class="card">
    <header class="brand">
      <div class="brand-mark"></div>
      <h1 class="brand-name">Corvane<br>Industries<span class="brand-suffix">Pty Ltd</span></h1>
    </header>

    <h2 class="person">Marla Quinlan</h2>

    <ul class="contact-list">
      <li>
        <svg class="contact-icon" viewBox="0 0 24 24" aria-label="Phone"><path d="M6.6 10.8a15 15 0 0 0 6.6 6.6l2.2-2.2a1 1 0 0 1 1-.25 11.4 11.4 0 0 0 3.6.57 1 1 0 0 1 1 1V20a1 1 0 0 1-1 1A17 17 0 0 1 3 4a1 1 0 0 1 1-1h3.5a1 1 0 0 1 1 1c0 1.25.2 2.45.57 3.57a1 1 0 0 1-.25 1z"/></svg>
        61 7 3000 4821
      </li>
      <li>
        <svg class="contact-icon" viewBox="0 0 24 24" aria-label="Mobile"><path d="M7 1h10a2 2 0 0 1 2 2v18a2 2 0 0 1-2 2H7a2 2 0 0 1-2-2V3a2 2 0 0 1 2-2zm0 3v14h10V4z"/></svg>
        61 400 555 218
      </li>
      <li>
        <svg class="contact-icon" viewBox="0 0 24 24" aria-label="Fax"><path d="M6 2h9l3 3v5H6zM3 11h18a1 1 0 0 1 1 1v8a1 1 0 0 1-1 1H3a1 1 0 0 1-1-1v-8a1 1 0 0 1 1-1z"/></svg>
        61 7 3000 4822
      </li>
    </ul>

    <address class="address">
      <span>14 Tallow Street, Hemmant QLD 4174</span>
      <span class="po">PO Box 582, Morningside QLD 4170</span>
    </address>

    <div class="website">www.corvane-industries.com.au</div>
    <div class="email">marla@corvane-industries.com.au</div>
  </article>
</body>
</html>
```